Certificate of Completion - Educational Trainings

We are looking for a certificate of completion for individuals who complete one of our specific trainings. Files should be provided in a Word (docx) or PowerPoint (pptx) format. The "Talmoray example.png" file is to show necessary information. Copies of logos have been included for design purposes.

Target Market(s)

Training Participants

Industry/Entity Type

Healthcare

Font styles to use
Sans Serif

```html
<!DOCTYPE html>
<html lang="en">
<head>
<meta charset="utf-8">
<title>Talmoray Certificate of Completion</title>
<link href="https://fonts.googleapis.com/css2?family=Antonio:wght@300;500&family=Montserrat:wght@800&family=Pinyon+Script&family=Roboto:ital,wght@0,300;0,400;0,700;1,400&display=swap" rel="stylesheet">
<style>
  :root{
    --backdrop:#f0f1f3;
    --paper:#ffffff;
    --green-deep:#176937;
    --green-leaf:#6ab04c;
    --edge-tint:#eef5ec;
    --ink:#111111;
  }
  *{margin:0;padding:0;box-sizing:border-box}
  html,body{width:1200px;height:1000px;overflow:hidden;background:var(--backdrop)}
  .certificate{
    position:absolute;left:205px;top:194px;width:790px;height:611px;
    background:var(--paper);
    box-shadow:0 8px 22px rgba(0,0,0,.18);
    font-family:"Roboto",sans-serif;color:var(--ink);
  }
  .edge{position:absolute;top:0;bottom:25px;width:25px;background:var(--edge-tint)}
  .edge--left{left:0}
  .edge--right{right:0}
  .side-bar{position:absolute;top:0;width:50px;height:262px;background:var(--green-deep)}
  .side-bar--left{left:89px}
  .side-bar--right{left:650px}
  .brand{position:absolute;left:0;right:0;top:28px;text-align:center}
  .brand-dot{display:block;margin:0 auto 14px;width:40px;height:40px;border-radius:50%;background:var(--green-deep)}
  .brand-name{font-family:"Montserrat",sans-serif;font-weight:800;font-size:28px;letter-spacing:3px;line-height:1}
  .sponsor-info{position:absolute;left:0;right:0;top:118px;text-align:center;font-weight:300;font-size:11.5px;line-height:14.5px}
  .display{position:absolute;left:0;top:0;width:790px;height:611px;overflow:visible}
  .title{font-family:"Antonio",sans-serif;font-weight:300;fill:var(--green-deep)}
  .subtitle{font-family:"Pinyon Script",cursive;fill:var(--green-leaf);font-weight:700}
  .awarded{font-family:"Antonio",sans-serif;font-weight:500;fill:var(--ink)}
  .recipient{font-family:"Pinyon Script",cursive;fill:var(--green-deep);font-weight:700}
  .recipient-rule{position:absolute;left:176px;top:423px;width:446px;height:2px;background:var(--green-deep)}
  .course-details{position:absolute;left:0;right:0;top:435px;text-align:center;font-style:italic;font-size:11.5px;line-height:14.4px}
  .signoff{position:absolute;right:89px;top:514px;text-align:right}
  .completion{font-weight:300;font-size:11px}
  .completion-date{font-size:17px;font-weight:400;margin-left:3px}
  .signer{display:inline-block;margin-top:3px;font-weight:700;font-size:17px;line-height:20px;border-bottom:1.5px solid var(--ink)}
  .signer-title{font-weight:300;font-size:11.5px;line-height:14px;margin-top:1px}
  .footer-band{
    position:absolute;left:0;right:0;bottom:0;height:25px;background:var(--green-deep);
    color:#fff;font-style:italic;font-size:10.6px;line-height:25px;text-align:center;white-space:nowrap;
  }
</style>
</head>
<body>
  <main class="certificate">
    <div class="edge edge--left"></div>
    <div class="edge edge--right"></div>
    <div class="side-bar side-bar--left"></div>
    <div class="side-bar side-bar--right"></div>

    <header class="brand">
      <span class="brand-dot"></span>
      <div class="brand-name">TALMORAY</div>
    </header>
    <p class="sponsor-info">48 HARBOR LANE, STE. 310 KESTREL BAY, ME 04120<br>CE SPONSOR COUNCIL NUMBER 57302</p>

    <svg class="display" viewBox="0 0 790 611">
      <text class="title" x="169" y="263" font-size="128" textLength="451" lengthAdjust="spacingAndGlyphs">CERTIFICATE</text>
      <text class="subtitle" x="395" y="303" font-size="40" text-anchor="middle" textLength="268" lengthAdjust="spacingAndGlyphs">of completion</text>
      <text class="awarded" x="183" y="357" font-size="42" textLength="423" lengthAdjust="spacingAndGlyphs">THIS CERTIFICATE IS AWARDED TO</text>
      <text class="recipient" x="165" y="405" font-size="50" textLength="440" lengthAdjust="spacingAndGlyphs">Marcus Whitfield</text>
    </svg>
    <div class="recipient-rule"></div>

    <p class="course-details">
      FOR SUCCESSFUL COMPLETION OF<br>
      BEST PRACTICES: BUDGET PROCESS/BUDGET BUILDING<br>
      COMPLETED ONLINE FIELD OF STUDY FINANCE<br>
      CPE CREDITS: 1
    </p>

    <section class="signoff">
      <div class="completion">COMPLETION DATE : <span class="completion-date">05/16/2024</span></div>
      <div class="signer">NORA BELCOURT</div>
      <div class="signer-title">SENIOR CONSULTANT</div>
    </section>

    <footer class="footer-band">IN ACCORDANCE WITH THE STANDARDS OF THE CONTINUING EDUCATION SPONSOR COUNCIL, CPE CREDITS HAVE BEEN GRANTED BASED ON A 50 MINUTE HOUR.</footer>
  </main>
</body>
</html>
```